Maple Hollow Bloom Backdrops Business card

Looking to have a business card design incorporating my logo for my flower wall business.

Industry/Entity Type

Wedding & event planning

Contact Information for Business Card

My business logo, my name - Jill Worthing (owner), my tagline - Let us be your something extra, phone # 401-627-3918, email address - maplehollowbloombackdrops@fernpost.com, my website - maplehollowbloombackdrops.com, Instagram handle- @maplehollowbloombackdrops, FB handle Handle - maplehollowbloombackdrops

Font styles to use
Other font styles liked:
• Sentaina is the font that is used in my logo

Requirements
Must have
• Would like a double sided business card

```html
<!DOCTYPE html>
<html lang="en">
<head>
<meta charset="utf-8">
<title>Maple Hollow Bloom Backdrops – Business Card</title>
<link href="https://fonts.googleapis.com/css2?family=Poppins:wght@300;400;600&display=swap" rel="stylesheet">
<style>
  :root {
    --page-bg: #e9e6e2;
    --card-dark: #2d2d2e;
    --card-light: #ffffff;
    --ink-dark: #222222;
    --ink-muted: #4a4a4a;
    --ink-light: #ffffff;
    --accent-pink: #d1298f;
    --accent-pink-soft: #e07ab6;
    --accent-gold: #d9b451;
  }
  * { margin: 0; padding: 0; box-sizing: border-box; }
  html, body {
    width: 1200px; height: 900px; overflow: hidden;
    background: var(--page-bg);
    font-family: "Poppins", sans-serif;
  }
  .canvas {
    position: relative; width: 1200px; height: 900px;
    display: flex; flex-direction: column; align-items: center; justify-content: center; gap: 40px;
  }
  .card {
    position: relative; width: 700px; height: 400px;
    border-radius: 22px; overflow: hidden;
    box-shadow: 0 8px 24px rgba(0,0,0,0.18);
  }
  .card--front { background: var(--card-dark); }
  .card--back { background: var(--card-light); }

  .brand-mark {
    position: absolute;
    display: flex; align-items: center; justify-content: center; text-align: center;
    border-radius: 50%;
    border: 2px solid var(--accent-gold);
    font-weight: 400; line-height: 1.25;
  }
  .card--front .brand-mark {
    width: 220px; height: 220px; left: 240px; top: 60px;
    color: var(--ink-light); font-size: 22px;
  }
  .card--back .brand-mark {
    width: 200px; height: 200px; left: 450px; top: 36px;
    color: var(--ink-dark); font-size: 20px;
  }
  .tagline {
    position: absolute; left: 0; right: 0; top: 318px;
    text-align: center; color: var(--ink-light);
    font-size: 20px; font-weight: 300; letter-spacing: 0.3px;
  }

  .person { position: absolute; left: 44px; top: 150px; }
  .person__name { font-size: 28px; color: var(--accent-pink-soft); font-weight: 300; line-height: 1.1; }
  .person__name strong { color: var(--accent-pink); font-weight: 600; }
  .person__role { font-size: 17px; color: var(--ink-muted); font-weight: 300; }

  .contacts { position: absolute; left: 44px; top: 232px; list-style: none; }
  .contacts li {
    display: flex; align-items: center; gap: 12px;
    font-size: 16px; color: var(--ink-muted); font-weight: 300; line-height: 1.55;
  }
  .contacts li.gap-top { margin-top: 12px; }
  .contacts .icon { width: 14px; height: 14px; flex: none; }
  .contacts .dot { width: 7px; height: 7px; margin: 0 3.5px; border-radius: 50%; background: var(--accent-pink); flex: none; }

  .web-row {
    position: absolute; left: 44px; right: 36px; top: 356px;
    display: flex; align-items: center; gap: 12px;
  }
  .web-row__rule { flex: 1; height: 1px; background: var(--accent-pink); }
  .web-row__url { font-size: 16px; color: var(--accent-pink); font-weight: 300; }
  .web-row__url strong { font-weight: 600; }
</style>
</head>
<body>
<main class="canvas">
  <section class="card card--front" aria-label="Card front">
    <div class="brand-mark">Maple Hollow<br>Bloom<br>Backdrops</div>
    <p class="tagline">Let us be your something extra</p>
  </section>

  <section class="card card--back" aria-label="Card back">
    <div class="brand-mark">Maple Hollow<br>Bloom<br>Backdrops</div>

    <div class="person">
      <p class="person__name">Jill <strong>Worthing</strong></p>
      <p class="person__role">owner</p>
    </div>

    <ul class="contacts">
      <li><span class="dot"></span>@maplehollowbloombackdrops</li>
      <li><span class="dot"></span>maplehollowbloombackdrops</li>
      <li class="gap-top">
        <svg class="icon" viewBox="0 0 24 24" aria-hidden="true"><path fill="#d1298f" d="M6.6 10.8a15.1 15.1 0 0 0 6.6 6.6l2.2-2.2a1 1 0 0 1 1-.25 11.4 11.4 0 0 0 3.6.57 1 1 0 0 1 1 1V20a1 1 0 0 1-1 1A17 17 0 0 1 3 4a1 1 0 0 1 1-1h3.5a1 1 0 0 1 1 1c0 1.25.2 2.45.57 3.57a1 1 0 0 1-.25 1z"/></svg>
        401-627-3918
      </li>
      <li>
        <svg class="icon" viewBox="0 0 24 24" aria-hidden="true"><rect x="3" y="5" width="18" height="14" rx="2" fill="none" stroke="#d1298f" stroke-width="2"/><path d="M3 7l9 6 9-6" fill="none" stroke="#d1298f" stroke-width="2"/></svg>
        maplehollowbloombackdrops@fernpost.com
      </li>
    </ul>

    <div class="web-row">
      <span class="web-row__rule"></span>
      <span class="web-row__url">www.<strong>maplehollowbloombackdrops.com</strong></span>
    </div>
  </section>
</main>
</body>
</html>
```